Thermostat Screen Design

We need a screen layout design for a new thermostat we're currently developing. If you're not familiar with thermostats, you can see some examples here - http://heating-dials-compared.bestlistguide.example/

We're after the main page design, with icons, colours etc. It needs to be clean, modern and minimalistic. Attached is all components required on the screen. The screen size is 5 inch (diagnol).

The arrows on the screen showcase what happens when you press a button. For example, when you press MODE once you get OFF, press it twice, HEAT, press it 3 times, COOL, etc. This is just for your reference.

You have complete creative license on how you choose to layout the screen, position the components etc, but we require:

- it must be on a 5 inch screen diagnol
- modern, clean and minimalistic
- includes icons and colours
- Intuitive

Let me know if any questions.

```html
<!DOCTYPE html>
<html lang="en">
<head>
<meta charset="utf-8">
<title>Thermostat Screen Design</title>
<link rel="stylesheet" href="https://fonts.googleapis.com/css2?family=Open+Sans:wght@300;400&display=swap">
<style>
  :root {
    --page-bg: #ecebe8;
    --text: #ffffff;
    --bar-day: #1d4a66;
    --bar-dusk: #3a2340;
    --photo-day-top: #6fb9e6;
    --photo-day-bottom: #7bbf45;
    --photo-dusk-top: #8e4f9e;
    --photo-dusk-bottom: #b27bb0;
    --nav-day: rgba(8, 20, 6, 0.88);
    --nav-day-mode: rgba(0, 0, 0, 0.55);
    --nav-dusk: rgba(30, 26, 32, 0.92);
    --nav-dusk-mode: rgba(10, 8, 12, 0.5);
    --arrow: #8a5fa8;
  }
  * { box-sizing: border-box; margin: 0; padding: 0; }
  html, body { width: 1200px; height: 675px; overflow: hidden; }
  body {
    background: var(--page-bg);
    font-family: "Open Sans", "Segoe UI", sans-serif;
    color: var(--text);
    position: relative;
  }
  .screen {
    position: absolute;
    top: 160px;
    width: 560px;
    height: 356px;
    overflow: hidden;
  }
  .screen--day { left: 20px; }
  .screen--dusk { left: 620px; }

  .backdrop { position: absolute; inset: 0; }
  .screen--day .backdrop {
    background: linear-gradient(180deg, var(--photo-day-top) 0%, var(--photo-day-bottom) 100%);
  }
  .screen--dusk .backdrop {
    background: linear-gradient(180deg, var(--photo-dusk-top) 0%, var(--photo-dusk-bottom) 100%);
  }

  .status-bar {
    position: absolute; left: 0; top: 0; width: 100%; height: 37px;
    font-size: 12px;
  }
  .screen--day .status-bar { background: var(--bar-day); }
  .screen--dusk .status-bar { background: var(--bar-dusk); }
  .status-bar span {
    position: absolute; top: 0; line-height: 37px; transform: translateX(-50%);
  }

  .reading { position: absolute; font-weight: 300; line-height: 1; white-space: nowrap; }
  .room-label { left: 64px; top: 108px; font-size: 17px; }
  .room-value { left: 80px; top: 132px; font-size: 100px; letter-spacing: -6px; }
  .room-unit { left: 174px; top: 134px; font-size: 16px; }
  .outdoor-label { left: 222px; top: 179px; font-size: 10px; }
  .outdoor-value { left: 248px; top: 193px; font-size: 36px; }
  .outdoor-unit { left: 292px; top: 193px; font-size: 9px; }
  .sleep { left: 396px; top: 118px; font-size: 9px; display: flex; align-items: center; gap: 3px; }
  .clock { left: 394px; top: 143px; font-size: 29px; word-spacing: 14px; }
  .rh-label { left: 418px; top: 183px; font-size: 10.5px; }
  .rh-value { left: 467px; top: 180px; font-size: 35px; }

  .nav-bar {
    position: absolute; left: 0; bottom: 0; width: 100%; height: 54px;
    font-size: 12px;
  }
  .screen--day .nav-bar { background: var(--nav-day); }
  .screen--dusk .nav-bar { background: var(--nav-dusk); }
  .nav-mode {
    position: absolute; left: 0; top: 0; width: 129px; height: 100%;
  }
  .screen--day .nav-mode { background: var(--nav-day-mode); }
  .screen--dusk .nav-mode { background: var(--nav-dusk-mode); }
  .nav-bar .nav-item {
    position: absolute; top: 0; line-height: 54px; transform: translateX(-50%);
  }
  .nav-arrow { position: absolute; top: 22px; }
  .nav-arrow--prev { left: 22px; }
  .nav-arrow--next { left: 100px; }
</style>
</head>
<body>

<section class="screen screen--day">
  <div class="backdrop" role="img" aria-label="Background photo: a house with trees and lawn under a blue sky"></div>
  <header class="status-bar">
    <span style="left:57px">12:14</span>
    <span style="left:197px">12/02/2014</span>
    <span style="left:347px">Wednesday</span>
    <span style="left:500px">Zone02</span>
  </header>
  <div class="reading room-label">Room Temperature</div>
  <div class="reading room-value">18</div>
  <div class="reading room-unit">°C</div>
  <div class="reading outdoor-label">Outdoor Temperature</div>
  <div class="reading outdoor-value">22</div>
  <div class="reading outdoor-unit">°C</div>
  <div class="reading sleep">
    <svg width="18" height="16" viewBox="0 0 18 16" aria-hidden="true"><path d="M8 3a6 6 0 1 0 6 8A5 5 0 0 1 8 3z" fill="#fff"/><path d="M13 1l.6 1.4L15 3l-1.4.6L13 5l-.6-1.4L11 3l1.4-.6zM16 5.5l.4.9.9.4-.9.4-.4.9-.4-.9-.9-.4.9-.4z" fill="#fff"/></svg>
    Sleep Mode
  </div>
  <div class="reading clock">12:14 AM</div>
  <div class="reading rh-label">Indoor RH</div>
  <div class="reading rh-value">45%</div>
  <nav class="nav-bar">
    <div class="nav-mode"></div>
    <svg class="nav-arrow nav-arrow--prev" width="6" height="11" viewBox="0 0 6 11" aria-hidden="true"><path d="M6 0v11L0 5.5z" fill="var(--arrow)"/></svg>
    <span class="nav-item" style="left:64px">MODE</span>
    <svg class="nav-arrow nav-arrow--next" width="6" height="11" viewBox="0 0 6 11" aria-hidden="true"><path d="M0 0v11l6-5.5z" fill="var(--arrow)"/></svg>
    <span class="nav-item" style="left:187px">FAN</span>
    <span class="nav-item" style="left:323px">SETTINGS</span>
    <span class="nav-item" style="left:484px">ZONES</span>
  </nav>
</section>

<section class="screen screen--dusk">
  <div class="backdrop" role="img" aria-label="Background photo: a snowy mountain and forest under a pink dusk sky"></div>
  <header class="status-bar">
    <span style="left:57px">12:14</span>
    <span style="left:197px">12/02/2014</span>
    <span style="left:347px">Wednesday</span>
    <span style="left:500px">Zone02</span>
  </header>
  <div class="reading room-label">Room Temperature</div>
  <div class="reading room-value">18</div>
  <div class="reading room-unit">°C</div>
  <div class="reading outdoor-label">Outdoor Temperature</div>
  <div class="reading outdoor-value">22</div>
  <div class="reading outdoor-unit">°C</div>
  <div class="reading sleep">
    <svg width="18" height="16" viewBox="0 0 18 16" aria-hidden="true"><path d="M8 3a6 6 0 1 0 6 8A5 5 0 0 1 8 3z" fill="#fff"/><path d="M13 1l.6 1.4L15 3l-1.4.6L13 5l-.6-1.4L11 3l1.4-.6zM16 5.5l.4.9.9.4-.9.4-.4.9-.4-.9-.9-.4.9-.4z" fill="#fff"/></svg>
    Sleep Mode
  </div>
  <div class="reading clock">12:14 AM</div>
  <div class="reading rh-label">Indoor RH</div>
  <div class="reading rh-value">45%</div>
  <nav class="nav-bar">
    <div class="nav-mode"></div>
    <svg class="nav-arrow nav-arrow--prev" width="6" height="11" viewBox="0 0 6 11" aria-hidden="true"><path d="M6 0v11L0 5.5z" fill="var(--arrow)"/></svg>
    <span class="nav-item" style="left:64px">MODE</span>
    <svg class="nav-arrow nav-arrow--next" width="6" height="11" viewBox="0 0 6 11" aria-hidden="true"><path d="M0 0v11l6-5.5z" fill="var(--arrow)"/></svg>
    <span class="nav-item" style="left:187px">FAN</span>
    <span class="nav-item" style="left:323px">SETTINGS</span>
    <span class="nav-item" style="left:484px">ZONES</span>
  </nav>
</section>

</body>
</html>
```